Carwash Signage

We own and operate a 25m tunnel car wash in the uk. We are looking to upgrade our signage to include the following:-

Wash selection Board Size-1300x1300mm
Conditions 1300x1300mm
Instructions 1300x1300mm
Banner 2600x600mm
Stamp card flyer a5 double sided - 9 squares for stamping 3rd square needs to say free air freshener 9th square needs to say free vip car wash.

I have attached some notes for the details that are required to be included.

We are looking for a modern smart look more European car wash style than American car wash style. It should be bold and clear. with yellow/orange & blue/green,grey colours

The final design must be in a industry standard printable format.

UPDATED BRIEF AS DISCUSSED: We require design for 2 x window decals, flag design and 50% off voucher. Attached are rough layout drawings of what they should look like - we expect the designs to be in keeping with the previous designs colours, etc that have been carried out. We Look forward to hearing from you.

Target Market(s)

local car owners within a 15-20 mile radius

Colors
0054AA
0677BA
7BADD7
CADEEF
E8F1F8
0094D4
00A9DD
6FCCEA
C7EBF8
E9F6FB
00AB8E
00BBA5
67D7C9
C6EFE9
E9F9F6

Requirements
Must have
• must be sharp and modern European look

```html
<!DOCTYPE html>
<html lang="en">
<head>
<meta charset="UTF-8">
<title>Instructions – Harbourside Car Wash</title>
<link rel="stylesheet" href="https://fonts.googleapis.com/css2?family=Archivo+Black&family=Figtree:wght@500;600&display=swap">
<style>
  :root {
    --sky-light: #5bb5fb;
    --sky-mid: #3f86dc;
    --sky-deep: #23409a;
    --title-navy: #0a3f8f;
    --panel: #ffffff;
    --copy-blue: #3a63b5;
    --bullet-ring: #2f86c9;
    --bullet-fill: #9fdcf5;
    --foam-top: #ffffff;
    --foam-mid: #b5e6f9;
    --foam-low: #5cc8f7;
  }
  html, body {
    margin: 0;
    padding: 0;
    width: 1200px;
    height: 1200px;
    overflow: hidden;
  }
  .sign {
    position: relative;
    width: 1200px;
    height: 1200px;
    overflow: hidden;
    background: linear-gradient(160deg, var(--sky-light) 0%, var(--sky-mid) 45%, var(--sky-deep) 100%);
    font-family: "Figtree", Arial, sans-serif;
  }
  .sign__swirl {
    position: absolute;
    inset: 0;
    width: 1200px;
    height: 1200px;
  }
  .sign__title {
    position: absolute;
    top: 86px;
    left: 0;
    width: 1200px;
    margin: 0;
    text-align: center;
    font-family: "Archivo Black", "Arial Black", sans-serif;
    font-size: 100px;
    line-height: 1;
    letter-spacing: -3px;
    color: var(--title-navy);
    -webkit-text-stroke: 3px var(--panel);
    paint-order: stroke fill;
    text-shadow: 4px 4px 0 rgba(255,255,255,0.55);
    z-index: 3;
  }
  .panel {
    position: absolute;
    left: 79px;
    top: 186px;
    width: 1042px;
    height: 794px;
    background: var(--panel);
    border-radius: 76px;
    z-index: 2;
  }
  .steps {
    position: absolute;
    left: 0;
    top: 0;
    margin: 0;
    padding: 0;
    list-style: none;
    color: var(--copy-blue);
    font-weight: 600;
    font-size: 29px;
    line-height: 35px;
    letter-spacing: -0.4px;
  }
  .step {
    position: absolute;
    left: 78px;
    white-space: nowrap;
  }
  .step::before {
    content: "";
    position: absolute;
    left: -48px;
    top: 6px;
    width: 32px;
    height: 18px;
    border-radius: 16px 16px 8px 8px;
    background: var(--bullet-fill);
    border: 2px solid var(--bullet-ring);
  }
  .checklist {
    position: absolute;
    margin: 0;
    padding: 0;
    list-style: none;
    color: var(--copy-blue);
    font-weight: 600;
    font-size: 27px;
    line-height: 32px;
    letter-spacing: -0.3px;
  }
  .check {
    position: absolute;
    white-space: nowrap;
    padding-left: 20px;
  }
  .check::before {
    content: "";
    position: absolute;
    left: 0;
    top: 11px;
    width: 8px;
    height: 8px;
    border-radius: 50%;
    background: var(--bullet-fill);
    border: 2px solid var(--bullet-ring);
  }
  .brand {
    position: absolute;
    right: 46px;
    top: 690px;
    display: flex;
    align-items: center;
    gap: 12px;
    color: var(--copy-blue);
    font-family: "Figtree", Arial, sans-serif;
    font-weight: 600;
    font-size: 30px;
    line-height: 1;
    white-space: nowrap;
  }
  .brand__dot {
    flex: none;
    width: 32px;
    height: 32px;
    border-radius: 50%;
    background: var(--copy-blue);
  }
  .foam {
    position: absolute;
    left: 0;
    bottom: 0;
    width: 1200px;
    height: 215px;
    background: linear-gradient(180deg, var(--foam-top) 0%, var(--foam-mid) 45%, var(--foam-low) 100%);
    border-radius: 60% 60% 0 0 / 40px 40px 0 0;
    z-index: 1;
  }
</style>
</head>
<body>
<main class="sign">
  <svg class="sign__swirl" viewBox="0 0 1200 1200" aria-hidden="true">
    <path d="M0 260 C 300 80, 700 20, 1200 180 L1200 0 L0 0 Z" fill="#6cc0fc" opacity="0.35"/>
    <path d="M0 1050 C 200 700, 500 520, 1200 600 L1200 1200 L0 1200 Z" fill="#1f3d94" opacity="0.35"/>
    <path d="M1200 820 C 1150 600, 1100 400, 980 230" stroke="#7bb8f0" stroke-width="40" fill="none" opacity="0.25"/>
  </svg>

  <h1 class="sign__title">INSTRUCTIONS</h1>

  <section class="panel">
    <ol class="steps">
      <li class="step" style="top:36px">Check for loose items before entering the wash</li>
      <li class="step" style="top:91px">Lower aerial if electrical make sure the aerial is fully retracted<br>Operator may assist but is not responsible for the condition of your car.</li>
      <li class="step" style="top:190px">Lower aerial if electrical make sure the aerial is fully retracted<br>Drive forward untill operator tells you to stop</li>
      <li class="step" style="top:292px">Operator will guide you into the carwash</li>
      <li class="step" style="top:354px">Once on conveyor track:</li>
      <li class="step" style="top:513px">Do not brake</li>
      <li class="step" style="top:568px">Do not steer</li>
      <li class="step" style="top:621px">Do not attempt exit vehicle</li>
      <li class="step" style="top:675px">At the end of wash drive away when<br>traffic Light turns green</li>
    </ol>

    <ul class="checklist">
      <li class="check" style="left:88px;top:409px">Hand brake off</li>
      <li class="check" style="left:307px;top:409px">Select neutral gear</li>
      <li class="check" style="left:571px;top:409px">Close all windows and sunroof</li>
      <li class="check" style="left:147px;top:456px">Leave engine running</li>
      <li class="check" style="left:479px;top:456px">Turn auto wipers off</li>
    </ul>

    <div class="brand">
      <span class="brand__dot"></span>
      <span class="brand__name">Harbourside Car Wash</span>
    </div>
  </section>

  <div class="foam" role="img" aria-label="Illustration of soft white and light blue soap foam clouds with bubbles along the bottom edge"></div>
</main>
</body>
</html>
```